Create Design/GRAPHICS/TEXT FOR CORVELLE/E-COMMERCE PRODUCT

Hi,
I am looking for a designer to create a advertisement/images/text for a product that I sell on Corvelle.
The first attachment is a 3d rendering of the product that I sell and want to use as the main image of the design.
The second attachment is of a existing ad on Corvelle that you can use as a general idea of how I want the final graphic to look like.
The third and fourth attachments are of the text/graphics that I would like for you to include in the graphic.
Finally, the last attachment is my logo that I would like to include in the graphic.
Please feel free to get creative with this and if you have any questions please feel free to contact me.-
Update-I just added source files for logo as attachment six.
Thanks!
Target Market(s)
CORVELLE
Industry/Entity Type
Product

```html
<!DOCTYPE html>
<html lang="en">
<head>
<meta charset="utf-8">
<title>Hand Crafted BBQ Access Doors</title>
<link href="https://fonts.googleapis.com/css2?family=Montserrat:wght@300;400;500;700;800;900&display=swap" rel="stylesheet">
<style>
  :root {
    --ink: #2a2a2a;
    --ink-soft: #3a3a3a;
    --card-dark: #2b2b2b;
    --card-light-top: #f4f4f4;
    --card-light-bottom: #d9d9d9;
    --steel-light: #e6e7e8;
    --steel-mid: #b9bcbf;
    --steel-dark: #8d9094;
    --paper: #ffffff;
  }
  * { margin: 0; padding: 0; box-sizing: border-box; }
  html, body { width: 1091px; height: 1200px; overflow: hidden; background: var(--paper); }
  body { font-family: "Montserrat", sans-serif; color: var(--ink); position: relative; }

  .headline { position: absolute; left: 78px; top: 70px; }
  .headline h1 { font-weight: 900; font-size: 31px; line-height: 32px; letter-spacing: 0.3px; text-transform: uppercase; color: var(--ink); }
  .headline p { font-weight: 300; font-size: 25px; margin-top: 8px; color: var(--ink-soft); }

  .brand { position: absolute; left: 760px; top: 78px; width: 230px; text-align: center; color: var(--ink); }
  .brand-name { font-weight: 500; font-size: 52px; letter-spacing: 3px; line-height: 1; }
  .brand-tag { font-weight: 500; font-size: 17px; letter-spacing: 2px; margin-top: 6px; }

  .product-render {
    position: absolute; left: 358px; top: 273px; width: 640px; height: 520px;
    background: radial-gradient(ellipse at 55% 50%, var(--steel-light) 0%, var(--steel-mid) 60%, var(--steel-dark) 100%);
    border-radius: 6px;
  }

  .features { position: absolute; left: 75px; top: 306px; width: 300px; list-style: none; }
  .features li { position: relative; padding-left: 28px; font-size: 19.5px; line-height: 24px; font-weight: 500; color: var(--ink); }
  .features li::before { content: ""; position: absolute; left: 2px; top: 7px; width: 11px; height: 11px; background: var(--ink); }
  .features li:nth-child(1) { top: 0; position: absolute; }
  .features li:nth-child(2) { top: 85px; position: absolute; }
  .features li:nth-child(3) { top: 170px; position: absolute; }
  .features li:nth-child(4) { top: 267px; position: absolute; }
  .features li:nth-child(5) { top: 348px; position: absolute; }
  .features li:nth-child(6) { top: 408px; position: absolute; }

  .values { position: absolute; left: 75px; top: 834px; display: flex; gap: 34px; }
  .value-card { width: 156px; height: 276px; border-radius: 18px; overflow: hidden; display: flex; flex-direction: column; }
  .value-emblem {
    height: 124px; background: linear-gradient(180deg, var(--card-light-top), var(--card-light-bottom));
    display: flex; align-items: center; justify-content: center; text-align: center; color: var(--ink);
  }
  .value-body { flex: 1; background: var(--card-dark); color: var(--paper); text-align: center; padding: 18px 12px 0; }
  .value-body h2 { font-weight: 800; font-size: 21px; letter-spacing: 0.2px; line-height: 1; }
  .value-body p { font-size: 12.5px; line-height: 15px; font-weight: 500; margin-top: 22px; }

  .seal { width: 96px; height: 96px; border-radius: 50%; background: var(--card-dark); }
  .emblem-wall { font-weight: 900; font-size: 25px; line-height: 26px; }
  .emblem-wall small { display: block; font-size: 10.5px; font-weight: 800; border-top: 2px solid var(--ink); padding-top: 3px; margin-top: 2px; letter-spacing: 0.5px; }
  .emblem-grade { font-weight: 800; font-size: 10px; }
  .emblem-grade .grade-box { display: block; background: var(--card-dark); color: var(--paper); font-size: 27px; font-weight: 900; padding: 3px 18px; margin: 5px auto; width: 104px; }
  .emblem-gauge { display: flex; font-weight: 800; font-size: 12px; line-height: 15px; text-align: left; gap: 4px; }
  .emblem-gauge .gauge-divider { width: 2px; height: 74px; background: var(--ink); }
</style>
</head>
<body>
  <header class="headline">
    <h1>Hand Crafted<br>BBQ Access Doors</h1>
    <p>Elegant Design with Double Construction</p>
  </header>

  <div class="brand">
    <div class="brand-name">ASHGROVE</div>
    <div class="brand-tag">outdoor kitchens</div>
  </div>

  <div class="product-render" role="img" aria-label="3D rendering of a stainless steel BBQ access door, open, with a paper towel holder on the inside of the door"></div>

  <ul class="features">
    <li>Premium 304 grade<br>stainless steel<br>construction</li>
    <li>Rugged 16-guage<br>square frame<br>construction</li>
    <li>DOUBLE WALL<br>Construction<br>-19 gauge outer wall<br>-20 guage outer wall</li>
    <li>Secure 4-point<br>magnetic closing<br>system</li>
    <li>HIgh quality 304 grade<br>stainless steel handles</li>
    <li>Convenient paper towel holder</li>
  </ul>

  <section class="values">
    <article class="value-card">
      <div class="value-emblem"><div class="seal"></div></div>
      <div class="value-body"><h2>QUALITY</h2><p>Our employees take Pride in their Work</p></div>
    </article>
    <article class="value-card">
      <div class="value-emblem"><div class="emblem-wall">DOUBLE<br>WALL<small>CONSTRUCTION</small></div></div>
      <div class="value-body"><h2>VALUE</h2><p>Our doors weigh 10 Pounds More than the competition</p></div>
    </article>
    <article class="value-card">
      <div class="value-emblem"><div class="emblem-grade">PREMIUM GRADE<span class="grade-box">304</span>STAINLESS STEEL</div></div>
      <div class="value-body"><h2>STRENGTH</h2><p>Offers higher level of Corrosion Resistance</p></div>
    </article>
    <article class="value-card">
      <div class="value-emblem"><div class="emblem-gauge"><span>16G<br>FRAME</span><span class="gauge-divider"></span><span><br>18G<br>OUTER<br>WALL</span></div></div>
      <div class="value-body"><h2>DURABILITY</h2><p>Thick and Durable Stainless Steel Construction</p></div>
    </article>
    <article class="value-card">
      <div class="value-emblem"><div class="seal"></div></div>
      <div class="value-body"><h2>PEACE<br>OF MIND</h2><p style="margin-top:12px">Your Satisfaction is our highest priority</p></div>
    </article>
  </section>
</body>
</html>
```